Powerpoint design template for PLAYNOVA for new digital platform

We would like to use a PowerPoint template, we would like to create a new page, we would like to create a new digital platform PLAYNOVA for schools and parents for the creation of playful communication and educational tools for children to enhance their positive development, amaze them learn in a playful way. This platform is going to be the most creative, stimulating and innovative classroom, easy to use and fast to implement. Scrapbooking, collages ... Magazine, newsletters Diplomla / awards Slideshows Facebook Calendars Organizers Greetings Games ... This powerpoint template will be used essential to We are looking for a professional design, positioning our brand in the children market with an adult hearing. so you will need to find a good deal. Primary target: nurseries & schools from 0 to 18 years old and universities (in 2nd phase) Secondary target: small & medium businesses Third target: general public, and TPE If it is a color scheme, then it is suggested that it be marketed in Europe (UK, Italy, Spain) and in a 2nd Stage USA and other countries. multiple options for front page, insidious pages (multiple styles with limited text and extended text) and final contact page We need something to read, we can not do it too much, but we can not do it. , and inside pages aligned to our logo

Target Market(s)

Target 1; Education with teacher Target 2; parents and grandparents

Industry/Entity Type

Education

Font styles to use
Other font styles liked:
• not decided. but not too fancy

Requirements
Must have
• Multi page options for front page, page insides (multiple styles with limited text and extended text) and final page contact
Nice to have
• do not have a lot of ideas. We need something to read, we can not get away from it
Should not have
• not too fancy and busy: keep clarity & simplicity while reassuring on quality

```html
<!DOCTYPE html>
<html lang="en">
<head>
<meta charset="utf-8">
<title>PLAYNOVA – Company Presentation</title>
<link href="https://fonts.googleapis.com/css2?family=Lato:wght@400;700;900&family=Montserrat:wght@500&display=swap" rel="stylesheet">
<style>
  :root {
    --stage: #e4e6ea;
    --slide: #ffffff;
    --ink: #1d1d1b;
    --muted: #4a4a4a;
    --brand-blue: #1aa7d8;
    --brand-lime: #d6e04a;
    --brand-green: #8cc04b;
    --brand-pale: #c9dc6e;
  }
  * { margin: 0; padding: 0; box-sizing: border-box; }
  html, body {
    width: 1200px;
    height: 891px;
    overflow: hidden;
    background: var(--stage);
  }
  .slide {
    position: absolute;
    left: 0;
    top: 108px;
    width: 1200px;
    height: 675px;
    background: var(--slide);
    font-family: "Lato", sans-serif;
    color: var(--ink);
  }
  .page-marker {
    position: absolute;
    left: 1100px;
    top: 22px;
    width: 48px;
    height: 48px;
  }
  .cover-brand {
    position: absolute;
    left: 360px;
    top: 240px;
    width: 520px;
  }
  .cover-brand .name {
    display: flex;
    align-items: center;
    gap: 22px;
    font-family: "Lato", sans-serif;
    font-weight: 900;
    font-size: 88px;
    letter-spacing: 2px;
    color: var(--ink);
    line-height: 1;
  }
  .cover-brand .name .dot {
    width: 46px;
    height: 46px;
    background: var(--brand-lime);
    border-radius: 50%;
    flex: none;
  }
  .tagline {
    margin-top: 36px;
    margin-left: 10px;
    font-family: "Montserrat", sans-serif;
    font-weight: 500;
    font-size: 24px;
    letter-spacing: 7px;
    line-height: 1.3;
    color: var(--ink);
  }
  .footer {
    position: absolute;
    left: 77px;
    top: 632px;
    display: flex;
    align-items: center;
    font-size: 13px;
    color: var(--muted);
  }
  .footer .footer-brand {
    font-weight: 700;
    color: var(--ink);
    margin-right: 4px;
  }
  .footer-rule {
    position: absolute;
    left: 300px;
    top: 640px;
    width: 845px;
    height: 3px;
    background: linear-gradient(to right,
      var(--brand-lime) 0 56%,
      var(--brand-green) 56% 84%,
      var(--brand-pale) 84% 100%);
  }
</style>
</head>
<body>
  <main class="slide">
    <svg class="page-marker" viewBox="0 0 48 48" aria-label="Slide 1">
      <polygon points="24,0 48,24 24,48 0,24" fill="var(--brand-blue)"/>
      <text x="24" y="29" text-anchor="middle" font-family="Lato, sans-serif" font-weight="700" font-size="13" fill="#1d1d1b">1</text>
    </svg>

    <section class="cover-brand">
      <h1 class="name"><span class="dot"></span>PLAYNOVA</h1>
      <p class="tagline">YOUR TAGLINE<br>GOES HERE</p>
    </section>

    <footer class="footer">
      <span class="footer-brand">PLAYNOVA</span>| Company Presentation
    </footer>
    <div class="footer-rule"></div>
  </main>
</body>
</html>
```